Have Logo - Need Business Card Design!!!

I am looking for a business card design for a real estate development business. The company name is Corvane Property Group. I already have a logo created by Artisan Hive and would like this logo to be incorporated into the design. I have uploaded the files. The card needs to be professional, but visually interesting. Not necessary to be double-sided, but if you want to get creative and can think of something to put on the back then have at it.

Target Market(s)

The target audience for these business cards will be professionals in the real estate industry.

Industry/Entity Type

Real Estate

Requirements
Must have
• The business card must have all the necessary items for a business card, i.e. company name, our logo, name (however, not title necessary), office address, office phone number, cell number, fax number, website address, etc.

You can use the information below for the card:

Gregory L. Danforth
718 Ridgemont Avenue
San Francisco, California 94382

www.corvaneproperty.example
gdanforth@corvaneproperty.example
Office: 415-555-0143
Fax: 415-555-0147
Cell: 415-555-0186

```html
<!DOCTYPE html>
<html lang="en">
<head>
<meta charset="utf-8">
<title>Corvane Property Group – Business Card</title>
<link rel="stylesheet" href="https://fonts.googleapis.com/css2?family=Lato:wght@400&display=swap">
<style>
  :root {
    --page-bg: #dfe3e3;
    --card-bg: #f5f5f3;
    --navy: #1b2a86;
    --brand-green: #2a8a1f;
    --band-light: #33e400;
    --band-dark: #1a8500;
    --band-deep: #2bd400;
    --sketch-light: #f3f4f4;
    --sketch-mid: #dcdfe0;
  }
  html, body {
    margin: 0;
    padding: 0;
    width: 1200px;
    height: 741px;
    overflow: hidden;
    background: var(--page-bg);
    font-family: "Lato", sans-serif;
  }
  .card {
    position: absolute;
    left: 46px;
    top: 49px;
    width: 1106px;
    height: 631px;
    background: var(--card-bg);
    overflow: hidden;
  }
  .skyline-art {
    position: absolute;
    left: 0;
    top: 10px;
    width: 440px;
    height: 330px;
    background: radial-gradient(ellipse at 45% 45%, var(--sketch-mid) 0%, var(--sketch-light) 60%, var(--card-bg) 100%);
  }
  .brand-name {
    position: absolute;
    left: 534px;
    top: 86px;
    margin: 0;
    font-size: 42px;
    font-weight: 400;
    line-height: 50px;
    color: var(--brand-green);
    white-space: nowrap;
  }
  .agent-name {
    position: absolute;
    left: 530px;
    top: 230px;
    margin: 0;
    font-size: 39px;
    font-weight: 400;
    color: var(--navy);
  }
  .details {
    position: absolute;
    left: 533px;
    top: 326px;
    font-size: 26px;
    line-height: 36px;
    color: var(--navy);
  }
  .details p { margin: 0; }
  .details .online {
    margin-top: 6px;
    line-height: 33px;
  }
  .contact-band {
    position: absolute;
    left: 0;
    bottom: 0;
    width: 100%;
    height: 102px;
  }
  .contact-band .strip {
    position: relative;
    height: 50px;
    background: var(--band-light);
    display: flex;
    align-items: center;
    font-size: 28px;
    color: var(--navy);
  }
  .contact-band .base {
    height: 52px;
    background: linear-gradient(to bottom, var(--band-dark) 0%, var(--band-deep) 100%);
  }
  .phone { position: absolute; }
  .phone.office { left: 117px; }
  .phone.fax { left: 448px; }
  .phone.cell { left: 749px; }
</style>
</head>
<body>
  <div class="card">
    <div class="skyline-art" role="img" aria-label="Faint pencil sketch of a suspension bridge"></div>

    <p class="brand-name">Corvane Property Group</p>

    <h1 class="agent-name">Gregory L. Danforth</h1>

    <div class="details">
      <p>718 Ridgemont Avenue</p>
      <p>San Francisco, California 94382</p>
      <div class="online">
        <p>www.corvaneproperty.example</p>
        <p>gdanforth@corvaneproperty.example</p>
      </div>
    </div>

    <div class="contact-band">
      <div class="strip">
        <span class="phone office">Office: 415-555-0143</span>
        <span class="phone fax">Fax: 415-555-0147</span>
        <span class="phone cell">Cell: 415-555-0186</span>
      </div>
      <div class="base"></div>
    </div>
  </div>
</body>
</html>
```